Naturopath specialising in Children's Health

I have just started working in a new clinic where I will be predominantly treating children so I would like to rebrand with a business card that reflects this.

I would like a clever design which is subtly playful and will attract children and parents alike, while maintaining a professional look. It must also reflect that I utilize natural medicine - including herbal medicine and nutrition as part of my treatment. Employing the use of a plant or herb would be ideal. I had envisioned the image of a dandelion blowing in the wind (or being blown by a child) as a great combination of the playful yet natural medicine I am trying to ecompass in the card.

I would like to use yellow, orange, blue or green as the dominant colour for the card.

The front of the card should contain the logo and the words 'Maribel Stroud - Naturopath.'

The back of the card should contain the following details:
Maribel Stroud BHSc Nat, Dip RM
Naturopath, Herbalist, Nutritionist, Iridologist, Remedial Massage Therapist, Reiki Practitioner
0413 927 186
Willowfern Haven - (02) 9731 4068
maribel.stroud@kestrelmail.example
NHPA 81347

Industry/Entity Type

Clinic

```html
<!DOCTYPE html>
<html lang="en">
<head>
<meta charset="utf-8">
<title>Maribel Stroud Naturopath – Business Card</title>
<link rel="stylesheet" href="https://fonts.googleapis.com/css2?family=Cinzel:wght@500&family=Arimo:wght@400;700&display=swap">
<style>
  :root {
    --backdrop: #ece8e2;
    --card: #ffffff;
    --ink: #111111;
    --brand-blue: #1d3480;
    --brand-green: #3b8a2c;
    --leaf-soft: rgba(59, 138, 44, 0.16);
    --sky-soft: rgba(29, 52, 128, 0.14);
    --shadow: 0 10px 28px rgba(0, 0, 0, 0.16);
  }
  * { box-sizing: border-box; margin: 0; padding: 0; }
  html, body {
    width: 1200px;
    height: 900px;
    overflow: hidden;
    background: var(--backdrop);
  }
  .canvas {
    width: 1200px;
    height: 900px;
    display: flex;
    flex-direction: column;
    align-items: center;
    justify-content: center;
    gap: 40px;
  }
  .card {
    position: relative;
    width: 700px;
    height: 400px;
    background: var(--card);
    box-shadow: var(--shadow);
    overflow: hidden;
  }

  /* Wordmark */
  .wordmark {
    display: flex;
    flex-direction: column;
    align-items: center;
    font-family: "Cinzel", serif;
    font-weight: 500;
    color: var(--ink);
  }
  .wordmark__name {
    letter-spacing: 0.02em;
    line-height: 1;
  }
  .wordmark__role {
    display: flex;
    align-items: center;
    letter-spacing: 0.28em;
    line-height: 1;
  }
  .wordmark__rule {
    height: 2px;
    background: var(--ink);
  }
  .brand-square {
    background: var(--brand-blue);
    transform: rotate(45deg);
    border-radius: 4px;
  }

  /* Back (details side) */
  .card--back .brand-row {
    position: absolute;
    left: 56px;
    top: 40px;
    display: flex;
    align-items: center;
    gap: 22px;
  }
  .card--back .brand-square { width: 36px; height: 36px; }
  .card--back .wordmark__name { font-size: 30px; }
  .card--back .wordmark__role { font-size: 15px; margin-top: 4px; gap: 8px; }
  .card--back .wordmark__rule { width: 34px; }

  .watermark-square {
    position: absolute;
    right: -40px;
    top: -60px;
    width: 200px;
    height: 200px;
    border-radius: 18px;
    transform: rotate(45deg);
    background: linear-gradient(180deg, var(--sky-soft) 0%, var(--leaf-soft) 100%);
  }

  .details {
    position: absolute;
    left: 58px;
    top: 128px;
    font-family: "Arimo", sans-serif;
    color: var(--ink);
  }
  .details__name {
    font-size: 21px;
    font-weight: 700;
    margin-bottom: 8px;
  }
  .details__line {
    font-size: 15px;
    line-height: 1.36;
  }

  /* Front (logo side) */
  .card--front {
    display: flex;
    flex-direction: column;
    align-items: center;
    justify-content: center;
    gap: 34px;
  }
  .card--front .brand-square { width: 84px; height: 84px; }
  .card--front .wordmark__name { font-size: 46px; }
  .card--front .wordmark__role { font-size: 24px; margin-top: 6px; gap: 12px; }
  .card--front .wordmark__rule { width: 50px; }
</style>
</head>
<body>
<main class="canvas">

  <section class="card card--back" aria-label="Card back with contact details">
    <div class="watermark-square" aria-hidden="true"></div>
    <div class="brand-row">
      <div class="brand-square" aria-hidden="true"></div>
      <div class="wordmark">
        <span class="wordmark__name">Maribel Stroud</span>
        <span class="wordmark__role"><span class="wordmark__rule"></span>Naturopath<span class="wordmark__rule"></span></span>
      </div>
    </div>
    <div class="details">
      <p class="details__name">Maribel Stroud BHSc Nat, Dip RM</p>
      <p class="details__line">Naturopath, Herbalist,</p>
      <p class="details__line">Nutritionist, Iridologist,</p>
      <p class="details__line">Remedial Massage Therapist,</p>
      <p class="details__line">Reiki Practitioner</p>
      <p class="details__line">0413 927 186</p>
      <p class="details__line">Willowfern Haven - (02) 9731 4068</p>
      <p class="details__line">maribel.stroud@kestrelmail.example</p>
      <p class="details__line">NHPA 81347</p>
    </div>
  </section>

  <section class="card card--front" aria-label="Card front with brand name">
    <div class="brand-square" aria-hidden="true"></div>
    <div class="wordmark">
      <span class="wordmark__name">Maribel Stroud</span>
      <span class="wordmark__role"><span class="wordmark__rule"></span>Naturopath<span class="wordmark__rule"></span></span>
    </div>
  </section>

</main>
</body>
</html>
```